Professional
Carl Moberty
Managing Partner / Co-Owner
482 Pelloway Blvd, East
Mississauga, Ontario
K7P 2N8
tkorblew@harbourkeyfunds.ca
www.pivotgrainfinance.ca
Please create one business card per logo and colour attached in the uploaded file.
Underneath the title, you should add:
Agent Licence #Q47715860
Please use the existing logo uploaded.
Please create a business card using each of these colour schemes.

```html
<!DOCTYPE html>
<html lang="en">
<head>
<meta charset="utf-8">
<title>Pivotgrain Finance – Stationery Set</title>
<link rel="stylesheet" href="https://fonts.googleapis.com/css2?family=Arimo:wght@400;700&display=swap">
<style>
  :root {
    --board: #a9aaac;
    --ink: #0c0c0c;
    --paper: #ffffff;
    --white: #ffffff;
    --tab: #8a8a8a;
    --shadow: rgba(0,0,0,0.18);
  }
  * { margin: 0; padding: 0; box-sizing: border-box; }
  html, body { width: 1200px; height: 900px; overflow: hidden; }
  body { background: var(--board); font-family: "Arimo", Arial, sans-serif; position: relative; }
  address { font-style: normal; }

  .piece { position: absolute; box-shadow: 0 2px 6px var(--shadow); overflow: hidden; }

  /* partner lockup: name plus one plain square */
  .brand { display: flex; align-items: center; gap: 6px; color: var(--white); font-weight: 700; text-transform: uppercase; letter-spacing: 0.04em; line-height: 1; white-space: nowrap; }
  .brand-square { width: 12px; height: 12px; background: var(--white); flex: none; }

  /* company name set plainly in the text font */
  .company-name { color: var(--white); font-weight: 700; line-height: 1; white-space: nowrap; letter-spacing: 0.02em; }

  .small { font-size: 7px; line-height: 1.45; color: var(--white); white-space: nowrap; }

  /* letterhead */
  .letterhead { left: 90px; top: 151px; width: 520px; height: 654px; background: var(--paper); }
  .letterhead-band { height: 68px; background: var(--ink); position: relative; }
  .letterhead-band .brand { position: absolute; left: 22px; top: 28px; font-size: 8px; }
  .letterhead-band .company-name { position: absolute; left: 190px; top: 27px; font-size: 14px; }
  .letterhead-band .address { position: absolute; left: 355px; top: 25px; }

  /* vertical card */
  .card-vertical { left: 661px; top: 188px; width: 112px; height: 305px; background: var(--paper); }
  .card-vertical-top { height: 172px; background: var(--ink); position: relative; color: var(--white); }
  .card-vertical-top .brand { position: absolute; left: 14px; top: 56px; font-size: 6px; }
  .card-vertical-top .person { position: absolute; right: 9px; top: 126px; text-align: right; font-size: 6px; line-height: 1.45; white-space: nowrap; }
  .card-vertical-top .person strong { font-size: 7px; }
  .card-vertical .tab { position: absolute; right: 0; top: 124px; width: 5px; height: 34px; background: var(--tab); }
  .card-vertical .contact { padding: 14px 8px 0; color: var(--ink); font-size: 5.4px; line-height: 1.5; white-space: nowrap; }

  /* disc */
  .disc { left: 849px; top: 134px; width: 278px; height: 278px; border-radius: 50%; background: linear-gradient(to bottom, var(--ink) 50%, var(--paper) 50%); }
  .disc-hole { position: absolute; left: 119px; top: 119px; width: 40px; height: 40px; border-radius: 50%; background: var(--board); box-shadow: inset 0 0 0 7px #e4e4e4; }
  .disc .brand { position: absolute; left: 44px; top: 88px; font-size: 6.5px; }
  .disc .company-name { position: absolute; left: 152px; top: 88px; font-size: 9.5px; }

  /* envelope */
  .envelope { left: 642px; top: 634px; width: 534px; height: 171px; background: var(--paper); }
  .envelope-band { height: 66px; background: var(--ink); position: relative; }
  .envelope-band .company-name { position: absolute; left: 30px; top: 26px; font-size: 15px; }
  .envelope-band .address { position: absolute; left: 380px; top: 24px; }

  /* horizontal cards */
  .card-front { left: 24px; top: 517px; width: 244px; height: 146px; background: var(--ink); color: var(--white); }
  .card-front .brand { position: absolute; left: 16px; top: 20px; font-size: 6px; }
  .card-front .person { position: absolute; right: 16px; top: 22px; text-align: right; font-size: 6.5px; line-height: 1.45; white-space: nowrap; }
  .card-front .person strong { font-size: 7.5px; }
  .card-front .tab { position: absolute; right: 0; top: 24px; width: 5px; height: 30px; background: var(--tab); }
  .card-front .contact { position: absolute; left: 16px; top: 72px; font-size: 5.6px; line-height: 1.5; white-space: nowrap; }

  .card-back { left: 24px; top: 686px; width: 244px; height: 144px; background: var(--ink); color: var(--white); }
  .card-back .brand { position: absolute; left: 22px; top: 42px; font-size: 6px; }
  .card-back .company-name { position: absolute; left: 126px; top: 42px; font-size: 9.5px; }
  .card-back .web { position: absolute; left: 0; right: 0; bottom: 18px; text-align: center; font-size: 6px; }
</style>
</head>
<body>

  <section class="piece letterhead" aria-label="Letterhead">
    <header class="letterhead-band">
      <div class="brand"><span class="brand-square"></span>Harbourkey Funds</div>
      <div class="company-name">Pivotgrain Finance</div>
      <address class="address small">482 Pelloway Blvd, East<br>Mississauga, Ontario K7P 2N8</address>
    </header>
  </section>

  <section class="piece card-vertical" aria-label="Business card, vertical">
    <div class="card-vertical-top">
      <div class="brand"><span class="brand-square"></span>Harbourkey Funds</div>
      <div class="person">
        <strong>Carl Moberty</strong><br>
        Managing Partner / Co-Owner<br>
        Agent Licence #Q47715860
      </div>
    </div>
    <span class="tab"></span>
    <address class="contact">
      482 Pelloway Blvd, East<br>
      Mississauga, Ontario K7P 2N8<br>
      Cell: 416.555.0142<br>
      Tel: 905.555.0187<br>
      Fax: 905.555.0193<br>
      Email: tkorblew@harbourkeyfunds.ca
    </address>
  </section>

  <section class="piece disc" aria-label="Disc label">
    <div class="brand"><span class="brand-square"></span>Harbourkey Funds</div>
    <div class="company-name">Pivotgrain Finance</div>
    <span class="disc-hole"></span>
  </section>

  <section class="piece envelope" aria-label="Envelope">
    <header class="envelope-band">
      <div class="company-name">Pivotgrain Finance</div>
      <address class="address small">482 Pelloway Blvd, East<br>Mississauga, Ontario K7P 2N8</address>
    </header>
  </section>

  <section class="piece card-front" aria-label="Business card, front">
    <div class="brand"><span class="brand-square"></span>Harbourkey Funds</div>
    <div class="person">
      <strong>Carl Moberty</strong><br>
      Managing Partner / Co-Owner<br>
      Agent Licence #Q47715860
    </div>
    <span class="tab"></span>
    <address class="contact">
      482 Pelloway Blvd, East<br>
      Mississauga, Ontario K7P 2N8<br>
      Cell: 416.555.0142<br>
      Tel: 905.555.0187<br>
      Fax: 905.555.0193<br>
      Email: tkorblew@harbourkeyfunds.ca
    </address>
  </section>

  <section class="piece card-back" aria-label="Business card, back">
    <div class="brand"><span class="brand-square"></span>Harbourkey Funds</div>
    <div class="company-name">Pivotgrain Finance</div>
    <div class="web">www.pivotgrainfinance.ca</div>
  </section>

</body>
</html>
```